Plumwick website

Provide a website for a business that is an online farmstand for mostly organic farm products produced on our 9 farms and packaged at our mill. We will be targeting an urban and suburban audience that will be able know the farms where their food is grown and "pick" their food online. We want the site to feel to feel fresh and urbane. Winning logo attached.

The website will feature:

A section with descriptions, pictures and Google maps for the farms as well as the produce produced on each farm. We will want to establish a provenance to the mostly organic food we produce and sell - and visit the farms if they want. We want our customers to know where their food comes from without having to live on a farm. We will market products of local farmers in addition to our own. We'll need room for about 50 farm descriptions and about 5 product descriptions per farm.

A master growing schedule -- there should be room for about 5 products per farm.

An online store (maybe linked to the farm and product) descriptions

An about us section -- where we can tell our family's story and about the history of the mill where we package food and provide fulfillment

A section for links to other farming and food information

A section for legal notices
Updates

Project Deadline Extended
Reason: Holiday weekend for many in USA

Target Market(s)

Educated, urban market who wants quality food at fair prices.

Industry/Entity Type

Farm

```html
<!DOCTYPE html>
<html lang="en">
<head>
<meta charset="utf-8">
<title>Plumwick — Online Farmstand</title>
<link rel="stylesheet" href="https://fonts.googleapis.com/css2?family=Kanit:wght@500;600&family=PT+Sans:ital,wght@0,400;0,700;1,400&family=Tinos:ital@0;1&family=Kaushan+Script&display=swap">
<style>
  :root{
    --ink:#3a2830;
    --green:#6f9a1e;
    --rust:#a4470f;
    --text:#4d4a4b;
    --muted:#7a7778;
    --rule:#d9d6d6;
    --paper:#ffffff;
  }
  *{box-sizing:border-box;margin:0;padding:0}
  html,body{width:685px;height:1200px;overflow:hidden;background:var(--paper)}
  body{position:relative;font-family:"PT Sans",sans-serif;color:var(--text)}
  .abs{position:absolute}
  .display{font-family:"Kanit",sans-serif;font-weight:600;text-transform:uppercase;letter-spacing:.3px}
  .script{font-family:"Kaushan Script",cursive}
  .serif{font-family:"Tinos",serif}
  .green{color:var(--green)}

  /* header */
  .cart{left:86px;top:8px;font:italic 9px "Tinos",serif;color:var(--rust);display:flex;align-items:center;gap:3px}
  .cart span{color:var(--ink);font-style:normal}
  .social-mini{left:86px;top:53px;display:flex;gap:3px}
  .social-mini i{display:block;width:9px;height:9px;background:#8a8486}
  .brand{left:0;width:685px;top:14px;text-align:center;color:var(--ink)}
  .brand-dot{display:block;margin:0 auto 6px;width:20px;height:20px;border-radius:50%;background:var(--ink)}
  .brand-name{font-family:"Kanit",sans-serif;font-weight:600;font-size:16px;letter-spacing:1.5px}
  .phone{right:86px;top:53px;font-size:9px;color:var(--ink)}
  .nav{left:86px;width:513px;top:74px;height:24px;border-top:2px solid var(--ink);border-bottom:2px solid var(--ink);display:flex;justify-content:space-between;align-items:center;padding:0 13px}
  .nav a{font-family:"Kanit",sans-serif;font-weight:500;font-size:9px;color:var(--ink);text-decoration:none;text-transform:uppercase;letter-spacing:.2px}
  .nav a.is-active{color:var(--green)}

  /* hero */
  .hero-left{left:90px;top:140px;width:170px}
  .small{font-size:6.4px;line-height:8px;color:var(--muted)}
  .hero-left .script-title{font-size:24px;color:var(--ink);line-height:30px;margin-top:1px}
  .tag{font-family:"Kanit",sans-serif;font-weight:500;font-size:6px;color:var(--green);text-transform:uppercase;letter-spacing:.3px}
  .dotted{border-top:1.5px dotted var(--ink);width:88px}
  .hero-left .dotted{margin:24px 0 20px}
  .hero-left .small.dark{color:var(--text)}
  .hero-left .label{font-family:"Kanit",sans-serif;font-weight:500;font-size:8px;color:var(--green);margin-top:4px;letter-spacing:.3px}
  .slider-dots{display:flex;gap:2px;margin-top:14px}
  .slider-dots i{display:block;width:8px;height:8px;border-radius:50%;background:var(--green)}
  .food-wheel{left:253px;top:120px;width:188px;height:188px;border-radius:50%;background:conic-gradient(from 0deg,#c2952a 0 12%,#c8442a 12% 25%,#4f8a2a 25% 40%,#e7dfc8 40% 55%,#d7a08f 55% 72%,#b58048 72% 88%,#d8b46a 88% 100%)}
  .wheat-circle{left:400px;top:236px;width:64px;height:64px;border-radius:50%;border:2px solid #fff;background:radial-gradient(circle at 50% 30%,#6f9cc8,#c99a3c 70%)}
  .hero-right{left:454px;top:135px;width:146px;text-align:center;color:var(--ink)}
  .hero-right .kicker{font-size:8px}
  .hero-right .big{font-size:17px;line-height:18px}
  .hero-right .body{font-size:6.4px;line-height:8px;color:var(--text);margin-top:3px}
  .hero-right .dotted{width:120px;margin:13px auto 14px}
  .hero-right .pretium{font-size:23px;line-height:24px}
  .hero-note{left:471px;top:274px;width:130px;font-size:6.4px;line-height:8.5px;color:var(--text)}
  .hero-note::before{content:"";position:absolute;left:-7px;top:2px;width:5px;height:5px;border-radius:50%;background:var(--green)}

  /* welcome */
  .section-title{left:86px;width:513px;top:346px;display:flex;align-items:center;gap:10px;color:var(--ink)}
  .section-title::before,.section-title::after{content:"";flex:1;border-top:1.5px solid var(--ink)}
  .section-title h1{font-family:"Kanit",sans-serif;font-weight:600;font-size:16px;letter-spacing:.8px}
  .photo{border-radius:0}
  .photo-wheat{left:90px;top:394px;width:90px;height:99px;background:linear-gradient(#4d6a8c 0,#8aa0b4 30%,#c18e2c 42%,#9a6a1c 100%)}
  .photo-workers{left:505px;top:394px;width:90px;height:99px;background:linear-gradient(#4e4a40,#6d7b52 55%,#3f5a2a)}
  .welcome-lead{left:225px;top:387px;width:240px;text-align:center;font-size:8.4px;line-height:11px;color:var(--muted)}
  .welcome-head{left:180px;width:325px;top:432px;text-align:center;font-size:11px;color:var(--green)}
  .welcome-col{top:468px;width:120px;font-size:6.4px;line-height:8.5px;color:var(--ink)}
  .welcome-col.left{left:205px;text-align:right}
  .welcome-col.right{left:371px}
  .welcome-mark{left:335px;top:463px;width:16px;height:16px;border-radius:50%;border:1.5px solid var(--ink)}
  .hr{left:86px;width:513px;border-top:1px solid var(--rule)}

  /* products */
  .products{left:86px;top:537px;width:513px;height:166px;display:flex}
  .product{flex:1;position:relative;text-align:center;padding-top:11px}
  .product.is-hover{box-shadow:0 0 3px rgba(0,0,0,.25);background:#fff}
  .product .thumb{margin:0 auto;width:62px;height:56px;border-radius:6px}
  .product h3{font-size:7px;font-weight:700;color:#222;margin-top:20px}
  .product p{font-size:6.4px;line-height:8px;color:var(--muted);margin-top:8px}
  .product .price{font-size:8px;color:var(--ink);margin-top:3px}
  .add{display:inline-flex;align-items:center;gap:2px;margin-top:9px;height:10px;padding:0 4px;border:1px solid #bbb;border-radius:2px;font-size:5.5px;font-weight:700;color:var(--ink);background:#fff}
  .product.is-hover .add{background:var(--ink);color:#fff;border-color:var(--ink)}
  .t-rice{background:radial-gradient(circle,#f4efe0 40%,#fff 72%)}
  .t-eggs{background:radial-gradient(circle,#d79a5e 40%,#fff 72%)}
  .t-milk{background:linear-gradient(90deg,#fff 25%,#e9ecef 40%,#f6f7f8 60%,#fff 75%)}
  .t-meat{background:radial-gradient(circle,#b2303a 35%,#fff 70%)}
  .t-wheat{background:radial-gradient(circle,#d9a85a 30%,#fff 70%)}
  .t-fish{background:radial-gradient(ellipse,#8f9692 38%,#fff 70%)}

  /* banner */
  .banner{left:86px;width:513px;top:727px;height:33px;border-top:1px solid var(--ink);border-bottom:1px solid var(--ink);display:flex;align-items:center;padding-left:25px;gap:8px}
  .banner-icon{width:24px;height:24px;border-radius:50%;background:#dedcdc;display:flex;align-items:center;justify-content:center}
  .banner-text{font-size:9px;color:var(--rust);white-space:nowrap}
  .banner-text span{font-family:"Tinos",serif;color:var(--muted);font-size:10px}

  /* features */
  .feature{top:779px;width:150px;text-align:center}
  .feature .pic{width:150px;height:144px}
  .pic-field{background:linear-gradient(#9dbfdc 0,#e6eef3 28%,#6f8e3a 38%,#3f6224 100%)}
  .pic-lettuce{background:linear-gradient(135deg,#8eb04a,#b9cf6b 50%,#5d8230)}
  .pic-peppers{background:linear-gradient(135deg,#5f7f1e,#9bb33a 50%,#3e5a12)}
  .feature h2{font-family:"Kanit",sans-serif;font-weight:600;font-size:11px;color:var(--rust);margin-top:30px;letter-spacing:.4px}
  .feature .sub{display:flex;align-items:center;justify-content:center;gap:5px;font-size:8px;color:var(--ink);margin-top:-2px}
  .feature .sub::before,.feature .sub::after{content:"";width:14px;border-top:1px solid var(--ink)}
  .feature p{font-size:6.4px;line-height:8.5px;color:var(--ink);margin-top:8px}
  .details{display:flex;align-items:center;justify-content:center;margin-top:10px}
  .details::before,.details::after{content:"";width:18px;border-top:1px solid var(--ink)}
  .details span{display:block;padding:0 9px;height:16px;line-height:13px;border:1.5px solid var(--ink);font-family:"Kanit",sans-serif;font-weight:500;font-size:7px;color:var(--ink);letter-spacing:.6px}
  .details.is-active span{background:var(--ink);color:#fff}

  /* footer */
  .footer-rule{left:86px;width:513px;top:1056px;border-top:2px solid var(--ink)}
  .fcol{top:1076px}
  .fcol h4{font-family:"Tinos",serif;font-weight:400;font-size:10px;color:#222;margin-bottom:6px}
  .fcol p{font-size:6.4px;line-height:8.5px;color:var(--ink)}
  .input{margin-top:7px;width:110px;height:12px;border:1px solid #bbb;border-radius:3px;font-size:6px;color:#777;padding:1px 4px}
  .btn{display:inline-block;margin-top:5px;background:var(--ink);color:#fff;font-size:6px;padding:1px 6px;border-radius:2px}
  .follow li{list-style:none;display:flex;align-items:center;gap:5px;font-size:8px;color:var(--ink);margin-bottom:5px}
  .follow i{display:block;width:11px;height:11px;background:var(--ink)}
  .bottom-rule{left:86px;width:513px;top:1162px;border-top:1px solid var(--rule)}
  .bottom-nav{left:86px;top:1174px;display:flex;gap:11px;font-size:6.4px;color:var(--ink)}
  .bottom-nav .is-active{color:var(--green)}
  .copyright{right:86px;top:1174px;font-size:6.4px;color:var(--ink)}
</style>
</head>
<body>

<header>
  <div class="abs cart">
    <svg width="10" height="9" viewBox="0 0 10 9" aria-hidden="true"><path d="M1 3h8l-1 5H2z" fill="none" stroke="#3a2830"/><path d="M3 3l2-2 2 2" fill="none" stroke="#3a2830"/></svg>
    Shopping Cart <span>(00 items)</span>
  </div>
  <div class="abs social-mini"><i></i><i></i><i></i></div>
  <div class="abs brand"><span class="brand-dot"></span><div class="brand-name">PLUMWICK</div></div>
  <div class="abs phone">Call Us: 000-000-0000</div>
  <nav class="abs nav">
    <a class="is-active">Home</a><a>About</a><a>Store</a><a>Farms</a><a>Food</a><a>Master Growing Schedule</a><a>Leagal</a><a>Contact</a>
  </nav>
</header>

<section class="hero">
  <div class="abs hero-left">
    <p class="small">Sed feugiat mollis neque. Suspendisse potenti. Sed dui, consequat vel ultrices quis, faucibus</p>
    <div class="script script-title">integer eget</div>
    <div class="tag">Etiam non felis mi. Quisque feugiat.</div>
    <div class="dotted"></div>
    <p class="small dark">Sed feugiat mollis neque. Suspendisse potenti. Sed dui, consequat vel ultrices quis, faucibus iaculis nisi. Pellentesque sit amet eleifend augue.</p>
    <div class="label">PELLENTESQUE</div>
    <div class="slider-dots"><i></i><i></i><i></i></div>
  </div>
  <svg class="abs" style="left:212px;top:124px" width="64" height="24" viewBox="0 0 64 24" aria-hidden="true"><path d="M2 14 Q30 -6 58 16" fill="none" stroke="#3a2830" stroke-width="0.8"/><path d="M52 16l6 0-3-5" fill="none" stroke="#3a2830" stroke-width="0.8"/></svg>
  <div class="abs food-wheel" role="img" aria-label="Circle of grocery foods: breads, fruit, vegetables, meat, eggs and dairy"></div>
  <div class="abs wheat-circle" role="img" aria-label="Ripe wheat ears against a blue sky"></div>
  <div class="abs hero-right">
    <div class="serif kicker">Luctus et ultrices posuere cubilia</div>
    <div class="display big">Etiam et tellus</div>
    <div class="tag" style="font-size:7px">Nam quis • Fermentum</div>
    <p class="serif body">Sed feugiat mollis neque. Suspendisse potenti. Sed libero dui, consequat vel ultrices quis,</p>
    <div class="dotted"></div>
    <div class="tag" style="font-size:7px">Pellentesque</div>
    <div class="script pretium">pretium</div>
    <div class="tag">Vulputate pellentesque</div>
  </div>
  <p class="abs hero-note">Cras eget sollicitudin lectus. In vel turpis lacus, vitae fringilla urna. Etiam et tellus vel turpis cursus egestas ut vel risus.</p>
</section>

<section class="welcome">
  <div class="abs section-title"><h1>Welcome to Plumwick</h1></div>
  <div class="abs photo photo-wheat" role="img" aria-label="Golden wheat field under a cloudy sky"></div>
  <p class="abs serif welcome-lead">Vestibulum ante ipsum primis in faucibus orci luctus et ultrices posuere cubilia Curae; Vestibulum ac nibh eget enim sollicitudin tincidunt et ac lorem. Cras eget sollicitudin lectus.</p>
  <div class="abs display welcome-head">Etiam non felis mi. Quisque feugiat</div>
  <p class="abs welcome-col left">Sed feugiat mollis neque. Suspendisse potenti. Seddui, consequat vel ultrices quis, faucibus iaculis nisi.</p>
  <span class="abs welcome-mark"></span>
  <p class="abs welcome-col right">Etiam non felis mi. Quisque feugiat, lectus non feugiat consectetur, purus ipsum lobortis nisl, a sollicitudin</p>
  <div class="abs photo photo-workers" role="img" aria-label="Farm workers tending seedlings in a field"></div>
  <div class="abs hr" style="top:520px"></div>
</section>

<section class="abs products">
  <article class="product"><div class="thumb t-rice" role="img" aria-label="Heap of white rice"></div><h3>Product Name</h3><p>Sed feugiat mollis neque.<br>Suspendisse potenti.</p><div class="price">$ 00.00</div><span class="add">ADD <svg width="6" height="5" viewBox="0 0 6 5"><path d="M0 1h6l-1 4H1z" fill="currentColor"/></svg></span></article>
  <article class="product"><div class="thumb t-eggs" role="img" aria-label="Brown eggs"></div><h3>Product Name</h3><p>Sed feugiat mollis neque.<br>Suspendisse potenti.</p><div class="price">$ 00.00</div><span class="add">ADD <svg width="6" height="5" viewBox="0 0 6 5"><path d="M0 1h6l-1 4H1z" fill="currentColor"/></svg></span></article>
  <article class="product"><div class="thumb t-milk" role="img" aria-label="Glass of milk"></div><h3>Product Name</h3><p>Sed feugiat mollis neque.<br>Suspendisse potenti.</p><div class="price">$ 00.00</div><span class="add">ADD <svg width="6" height="5" viewBox="0 0 6 5"><path d="M0 1h6l-1 4H1z" fill="currentColor"/></svg></span></article>
  <article class="product is-hover"><div class="thumb t-meat" role="img" aria-label="Cuts of red meat with parsley"></div><h3>Product Name</h3><p>Sed feugiat mollis neque.<br>Suspendisse potenti.</p><div class="price">$ 00.00</div><span class="add">ADD <svg width="6" height="5" viewBox="0 0 6 5"><path d="M0 1h6l-1 4H1z" fill="currentColor"/></svg></span></article>
  <article class="product"><div class="thumb t-wheat" role="img" aria-label="Wheat ears"></div><h3>Product Name</h3><p>Sed feugiat mollis neque.<br>Suspendisse potenti.</p><div class="price">$ 00.00</div><span class="add">ADD <svg width="6" height="5" viewBox="0 0 6 5"><path d="M0 1h6l-1 4H1z" fill="currentColor"/></svg></span></article>
  <article class="product"><div class="thumb t-fish" role="img" aria-label="Two fresh fish"></div><h3>Product Name</h3><p>Sed feugiat mollis neque.<br>Suspendisse potenti.</p><div class="price">$ 00.00</div><span class="add">ADD <svg width="6" height="5" viewBox="0 0 6 5"><path d="M0 1h6l-1 4H1z" fill="currentColor"/></svg></span></article>
</section>

<aside class="abs banner">
  <span class="banner-icon"><svg width="12" height="11" viewBox="0 0 12 11" aria-hidden="true"><path d="M0 1h2l2 6h6l1-4H3" fill="none" stroke="#3a2830"/><circle cx="5" cy="9.5" r="1" fill="#3a2830"/><circle cx="9" cy="9.5" r="1" fill="#3a2830"/></svg></span>
  <span class="script banner-text">Etiam eros velit, rutrum in fringilla id, fermentum sit amet nulla : <span>faucibus orci luctus et ultrices</span></span>
</aside>

<section class="features">
  <article class="abs feature" style="left:94px">
    <div class="pic pic-field" role="img" aria-label="Rows of green crops stretching to the horizon"></div>
    <h2>Morbi adipiscing</h2>
    <div class="script sub">lorem laoreet ante</div>
    <p>Nam quis ligula a nibh fermentum venenatis vitae nec neque. Etiam non felis mi. Quisque feugiat,</p>
    <div class="details is-active"><span>DETAILS</span></div>
  </article>
  <article class="abs feature" style="left:267px">
    <div class="pic pic-lettuce" role="img" aria-label="Rows of fresh lettuce growing"></div>
    <h2>Morbi adipiscing</h2>
    <div class="script sub">lorem laoreet ante</div>
    <p>Nam quis ligula a nibh fermentum venenatis vitae nec neque. Etiam non felis mi.</p>
    <div class="details"><span>DETAILS</span></div>
  </article>
  <article class="abs feature" style="left:440px">
    <div class="pic pic-peppers" role="img" aria-label="Pile of green chili peppers"></div>
    <h2>Morbi adipiscing</h2>
    <div class="script sub">lorem laoreet ante</div>
    <p>Nam quis ligula a nibh fermentum venenatis vitae nec neque. Etiam non felis mi. Quisque feugiat,</p>
    <div class="details"><span>DETAILS</span></div>
  </article>
</section>

<footer>
  <div class="abs footer-rule"></div>
  <div class="abs fcol" style="left:90px;width:130px">
    <h4>Newsletter Signup</h4>
    <p>Sign up with your email to recieve our free newsletter monthly.</p>
    <div class="input">enter your email id</div>
    <span class="btn">Submit</span>
  </div>
  <div class="abs fcol" style="left:235px">
    <h4>Follow Us</h4>
    <ul class="follow"><li><i></i>Circlepage</li><li><i></i>Chirpline</li><li><i></i>Reelcast</li></ul>
  </div>
  <div class="abs fcol" style="left:334px;width:118px">
    <h4>Our Store</h4>
    <p>Sed feugiat mollis neque. Suspendisse potenti. Seddui, consequat vel ultrices quis, faucibus iaculis nisi.</p>
    <span class="btn">Details</span>
  </div>
  <div class="abs fcol" style="left:472px;width:125px">
    <h4>Contact Us</h4>
    <p>Sed feugiat mollis neque. Suspendisse potenti. Seddui, consequat vel</p>
    <p style="margin-top:7px"><b>Email:</b> loremipsum@loremipsum.com<br><b>Phone:</b> 000-000-0000</p>
  </div>
  <div class="abs bottom-rule"></div>
  <nav class="abs bottom-nav"><span class="is-active">Home</span><span>About</span><span>Store</span><span>Farms</span><span>Food</span><span>Master growing schedule</span><span>Leagal</span><span>Contact</span></nav>
  <div class="abs copyright">© Copyright 2013. All Rights Reserved</div>
</footer>

</body>
</html>
```